Environmentally friendly Home and Office cleaning service needs a logo and web design!

Maple Sparkle is a new startup looking for a logo and web design. We're base in Ottawa, Canada, and all of our products are eco-friendly, as well as being easy on the sensitivities of our clients.
We wash windows, walls, kitchens, bathrooms, dust, vacuum and wash floors on our hands and knees, and bring all of our own gear and supplies.
tidyroost.example was my last website. It's functional, not bad - but just isn't great. I'm looking for a simple design, with few links or clickable buttons.
Colours I will leave to your creative mind to decide. I just want to see something that is relevant to "Maple Sparkle."

Target Market(s)

Often it's women and gay men, ages 35-70
White collar government workers, usually with pets (cats, dogs)

Industry/Entity Type

Cleaning Service

Logo Text

Maple Sparkle

Number of Pages Required

1 page

Font styles to use
Sans Serif

Colors

Designer to choose colors to be used in the design.

Requirements
Must have
• Colour, pictures

```html
<!DOCTYPE html>
<html lang="en">
<head>
<meta charset="utf-8">
<title>Maple Sparkle — Eco-Friendly Cleaning in Ottawa</title>
<link rel="stylesheet" href="https://fonts.googleapis.com/css2?family=Raleway:wght@400;500;600;700&family=Roboto:wght@400;500;700;900&display=swap">
<style>
:root{
  --green:#58b147;
  --green-soft:rgba(120,190,100,.82);
  --green-bar:#69b55c;
  --orange:#f2731f;
  --orange-deep:#d9560e;
  --blue:#2c6fb7;
  --navy:#0e4a8a;
  --ink:#2b2b2b;
  --body:#555;
  --white:#fff;
}
*{box-sizing:border-box;margin:0;padding:0}
html,body{width:1200px;height:2740px;overflow:hidden}
body{font-family:"Raleway",Arial,sans-serif;color:var(--body);background:var(--white);position:relative}

/* Header + hero */
.hero{position:absolute;left:0;top:0;width:1200px;height:663px;
  background:linear-gradient(135deg,#e9ece8 0%,#f7f7f4 35%,#dfe3d8 60%,#c9d6a6 78%,#eef0ea 100%)}
.site-header{position:absolute;left:0;top:0;width:1200px;height:115px;background:var(--green-soft)}
.brand{position:absolute;left:86px;top:44px;display:flex;align-items:center;gap:12px;color:var(--white);
  font-family:"Raleway",sans-serif;font-weight:500;font-size:31px}
.brand-mark{width:26px;height:26px;border-radius:50%;background:var(--white)}
.social-top{position:absolute;right:30px;top:10px;display:flex;gap:14px}
.social-top span{width:14px;height:14px;border-radius:50%;background:var(--white)}
.header-phone{position:absolute;left:606px;top:66px;display:flex;align-items:center;gap:10px;color:var(--white);font-family:"Roboto",sans-serif;font-size:14px}
.search{position:absolute;left:783px;top:62px;width:230px;border-bottom:1px solid rgba(255,255,255,.8);padding-bottom:3px;
  color:var(--white);font-size:11px;display:flex;justify-content:space-between}
.menu{position:absolute;left:1040px;top:68px;display:flex;align-items:center;gap:10px;color:var(--white);font-size:13px}
.menu i{display:block;width:22px;height:3px;background:var(--white);box-shadow:0 7px 0 var(--white),0 -7px 0 var(--white)}
.hero-title{position:absolute;left:0;top:335px;width:1200px;text-align:center;color:var(--white);
  font-family:"Roboto",sans-serif;font-weight:900;font-size:41px;letter-spacing:-.5px;text-shadow:0 2px 6px rgba(0,0,0,.55)}

/* Services band */
.services{position:absolute;left:0;top:663px;width:1200px;height:202px;display:flex}
.service{width:200px;height:202px;color:var(--white);display:flex;flex-direction:column;align-items:center;justify-content:flex-start;padding-top:28px;
  font-family:"Roboto",sans-serif;font-size:25px}
.service svg{width:62px;height:62px;margin-bottom:12px}
.service.blue{background:var(--blue);clip-path:polygon(0 0,100% 0,100% 100%,0 82%)}
.service.orange{background:var(--orange);clip-path:polygon(0 0,100% 0,100% 82%,0 100%)}
.service.lead{justify-content:center;padding:0 0 30px;flex-direction:row;gap:8px;font-weight:900;font-size:26px}
.service.lead svg{width:30px;height:30px;margin:0}

/* Intro */
.intro{position:absolute;left:0;top:925px;width:1200px;text-align:center}
.intro h2{font-family:"Roboto",sans-serif;font-weight:700;font-size:29px;color:var(--ink)}
.intro h2 span{display:block;color:var(--orange);font-weight:400;margin-top:4px}
.divider{margin:22px auto 30px;width:260px;height:20px;display:flex;align-items:center;gap:10px}
.divider b{flex:1;height:1px;background:var(--blue)}
.divider i{width:12px;height:12px;border-radius:50%;background:var(--orange)}
.intro p{width:1030px;margin:0 auto 24px;font-size:15.5px;line-height:1.7}

/* Eco section */
.eco{position:absolute;left:0;top:1350px;width:1200px;height:364px;background:var(--orange-deep)}
.eco-photo{position:absolute;right:0;top:0;width:420px;height:364px;background:linear-gradient(160deg,#e7d2c4 0%,#b89280 40%,#3c3330 100%)}
.eco-shade{position:absolute;left:0;top:0;width:860px;height:364px;background:linear-gradient(90deg,#d45510 0%,#e06318 70%,rgba(224,99,24,.2) 100%)}
.eco h3{position:absolute;left:90px;top:38px;color:var(--white);font-family:"Roboto",sans-serif;font-weight:500;font-size:28px}
.eco ul{position:absolute;left:96px;top:108px;list-style:none;color:var(--white);font-size:17px;line-height:1.55}
.eco li{position:relative;padding-left:30px;margin-bottom:16px}
.eco li::before{content:"";position:absolute;left:0;top:5px;width:14px;height:14px;border:1.5px solid var(--white);border-radius:50%}

/* How it works */
.how-photo{position:absolute;left:0;top:1714px;width:600px;height:593px;background:linear-gradient(140deg,#dcdcd2 0%,#f0efe9 40%,#b8936a 80%,#a47a50 100%)}
.how{position:absolute;left:447px;top:1781px;width:753px;height:484px;background:var(--green);color:var(--white);padding:30px 36px 0 36px}
.how h3{font-family:"Raleway",sans-serif;font-weight:700;font-size:30px}
.how h4{font-family:"Raleway",sans-serif;font-weight:700;font-size:20px;margin:2px 0 10px 4px}
.how .rule{width:90px;height:2px;background:var(--orange);margin:0 0 26px 4px}
.how p{font-size:14.5px;line-height:1.75;margin-bottom:22px;padding-left:44px;position:relative}
.how p.point svg{position:absolute;left:0;top:0;width:36px;height:26px}

/* About */
.about{position:absolute;left:86px;top:2370px;width:1030px}
.about h3{font-family:"Raleway",sans-serif;font-weight:700;font-size:25px;color:var(--navy);margin-bottom:14px}
.about p{font-size:12.5px;line-height:2;color:var(--ink)}

/* Footer */
.footer{position:absolute;left:0;top:2583px;width:1200px;height:110px;background:var(--navy)}
.pill{position:absolute;top:36px;height:44px;border:1.5px solid rgba(255,255,255,.7);border-radius:22px;color:var(--white);
  display:flex;align-items:center;justify-content:center;gap:14px;font-family:"Roboto",sans-serif;font-size:18px}
.pill.phone{left:86px;width:216px}
.pill.mail{left:440px;width:320px}
.pill.social{left:897px;width:216px;gap:24px}
.pill.social span{width:16px;height:16px;border-radius:50%;background:var(--white)}
.copyright{position:absolute;left:0;top:2693px;width:1200px;height:47px;background:var(--green-bar);color:var(--white);font-size:12px;display:flex;align-items:center;justify-content:center}
</style>
</head>
<body>

<section class="hero" role="img" aria-label="Photo of a bright living room with a cleaner mopping the floor beside a cart of cleaning supplies">
</section>

<header class="site-header">
  <div class="brand"><span class="brand-mark"></span>Maple Sparkle</div>
  <div class="social-top"><span></span><span></span><span></span><span></span></div>
  <div class="header-phone">
    <svg width="22" height="18" viewBox="0 0 22 18" fill="#fff"><path d="M2 6c0-3 4-5 9-5s9 2 9 5l-4 1-1-2H7L6 7 2 6z"/><rect x="5" y="8" width="12" height="9" rx="2"/></svg>
    613-555-0182
  </div>
  <div class="search"><span>Search</span>
    <svg width="11" height="11" viewBox="0 0 11 11" fill="none" stroke="#fff" stroke-width="1.6"><circle cx="4.5" cy="4.5" r="3.5"/><path d="M7 7l3 3"/></svg>
  </div>
  <div class="menu">Menu <i></i></div>
</header>

<h1 class="hero-title">WELCOME TO MAPLE SPARKLE</h1>

<nav class="services">
  <div class="service blue lead">WE WASH
    <svg viewBox="0 0 30 30" fill="#fff"><path d="M2 11h14V4l12 11-12 11v-7H2z"/></svg>
  </div>
  <div class="service orange">
    <svg viewBox="0 0 62 62" fill="none" stroke="#fff" stroke-width="2.4"><rect x="8" y="24" width="46" height="26" rx="3"/><path d="M8 33h46M31 33v17M24 24v-8a6 6 0 0 1 12 0M14 50v5M48 50v5"/></svg>
    Kitchens</div>
  <div class="service blue">
    <svg viewBox="0 0 62 62" fill="none" stroke="#fff" stroke-width="2.4"><path d="M6 30h50v6a12 12 0 0 1-12 12H18A12 12 0 0 1 6 36z"/><path d="M14 30V12a5 5 0 0 1 10 0M18 48l-3 6M44 48l3 6"/></svg>
    Bathrooms</div>
  <div class="service orange">
    <svg viewBox="0 0 62 62" fill="none" stroke="#fff" stroke-width="2.4"><ellipse cx="28" cy="40" rx="20" ry="12"/><circle cx="46" cy="44" r="8"/><path d="M20 30c4-10 14-18 26-18h8"/></svg>
    Floors</div>
  <div class="service blue">
    <svg viewBox="0 0 62 62" fill="none" stroke="#fff" stroke-width="2.4"><path d="M14 56V22a17 17 0 0 1 34 0v34z"/><path d="M31 6v50M14 28h34M14 42h34M10 56h42"/></svg>
    Windows</div>
  <div class="service orange">
    <svg viewBox="0 0 62 62" fill="#fff"><path d="M6 20l26-10 24 10-26 10z"/><path d="M6 30l24 10 26-10v5L30 46 6 35z"/><path d="M6 40l24 10 26-10v5L30 56 6 45z"/></svg>
    Walls</div>
</nav>

<section class="intro">
  <h2>LET US BE PART OF YOUR TEAM TO KEEP<span>YOUR SPACE CLEAN!</span></h2>
  <div class="divider"><b></b><i></i><b></b></div>
  <p>We will give your home the respect it deserves with careful attention to detal and thorough work. It can be a relief to know that you can leave and come back and never have to worry about dusting, vacuuming, windows or walls.</p>
  <p>We do all of that for you!<br>You don’t even have to think about providing any materials for us since we supply all of our own gear and equipment, all of which is 100% eco-friend and kind on sensitivities.</p>
  <p>We are insured and have references available to confirm our work ethic and trustworthiness.</p>
</section>

<section class="eco">
  <div class="eco-photo" role="img" aria-label="Photo of a gloved hand wiping a kitchen counter with a cloth"></div>
  <div class="eco-shade"></div>
  <h3>What Makes Maple Sparkle Environmentally Friendly?</h3>
  <ul>
    <li>We use unscented, non-toxic, chemical-free cleaners</li>
    <li>We use vinegar as an antiseptic and deodorizer when needed,<br>as well as for windows and mirrors</li>
    <li>We use baking soda if we need more aggressive scrubbing</li>
    <li>We use a HEPA-filter vacuum for allergen relief</li>
  </ul>
</section>

<div class="how-photo" role="img" aria-label="Photo of a cleaning team dusting a fireplace and mopping a wooden floor"></div>
<section class="how">
  <h3>How it Works</h3>
  <h4>The first clean is half-off because:</h4>
  <div class="rule"></div>
  <p class="point"><svg viewBox="0 0 36 26" fill="none" stroke="#fff" stroke-width="1.6"><path d="M2 12h8l6-9c2 0 3 2 2 4l-2 5h14a2 2 0 0 1 0 4h-3a2 2 0 0 1 0 4h-3a2 2 0 0 1 0 4H10l-8-2z"/></svg>We don’t give estimates. Houses can be very deceiving, and we don’t want to set inappropriate expectations. The discounted rate gives us the ability to estimate just how long regular cleans will take.</p>
  <p class="point"><svg viewBox="0 0 36 26" fill="none" stroke="#fff" stroke-width="1.6"><path d="M2 12h8l6-9c2 0 3 2 2 4l-2 5h14a2 2 0 0 1 0 4h-3a2 2 0 0 1 0 4h-3a2 2 0 0 1 0 4H10l-8-2z"/></svg>This also gives you the chance to test us out and see if we’re a good fit.</p>
  <p>For the first clean, it’d be ideal if you were there so that we can go room to room and make sure everything is exactly as you like it to be. I don’t want us leaving until you’re happy!</p>
  <p>Assuming you like what you see, we can then schedule regular appointments. I will have a copy of your keys made and initial them so that no one knows who these keys belong to (Anne Lowe would be “AL”).</p>
</section>

<section class="about">
  <h3>Who Am I?</h3>
  <p>Hi!<br>My name is Ellis Hart and I have been a professional cleaner in the Ottawa area for over 2 years, under the tutelage of Martin Alder, another professional with more than 15 years experience in the field. He taught me everything he knows about what clients want from their cleaners: a meticulous eye for detail, reliability and to always search for the difference that makes a difference in the client’s eyes.</p>
</section>

<footer class="footer">
  <div class="pill phone">
    <svg width="26" height="20" viewBox="0 0 22 18" fill="#fff"><path d="M2 6c0-3 4-5 9-5s9 2 9 5l-4 1-1-2H7L6 7 2 6z"/><rect x="5" y="8" width="12" height="9" rx="2"/></svg>
    613-555-0182</div>
  <div class="pill mail">
    <svg width="22" height="18" viewBox="0 0 22 18" fill="none" stroke="#fff" stroke-width="1.6"><rect x="1" y="3" width="20" height="14" rx="1"/><path d="M1 3l10 8 10-8"/></svg>
    Ellis.k.Hart@mail.example</div>
  <div class="pill social"><span></span><span></span><span></span><span></span></div>
</footer>
<div class="copyright">© Copyright 2017 Maple Sparkle | All Rights Reserved.</div>

</body>
</html>
```